Selkirk Boat Lines and Freight Business Card

I need business cards for my new water taxi and freight transport business I have started here in Kodiak Alaska. Kodiak is a remote island in the middle of the gulf of Alaska. There are seven native villages around the island and Kodiak is the #2 fishing port in the United States. We also have the largest Seaward Corps Base in the U.S. My company will be providing water taxi and freight transport logistics to the villages and many hunting and fishing lodges as well as remote properties around the island.

I would like a business card that isn't status quo, something that stands out, either in feel or appearance. I do like clean minimal designs but it needs to have the necessary contact info on it.

Target Market(s)

remote lodge / property owners, residents of the many villages around Kodiak and any one wanting to enjoy the great outdoors of Kodiak Alaska

Industry/Entity Type

Business

Contact Information for Business Card

I like clean simple designs that aren't cluttered but still provide the necessary information

Colors
0255a3
3277b5
33a4d5
9bcb3c
add136
fbed22
ffc214
f78f20
f37122

Requirements
Must have
• logo and contact info
• Captain Marcus Hollend
• www.selkirkboatlines.com
• marcus@selkirkboatlines.com

```html
<!DOCTYPE html>
<html lang="en">
<head>
<meta charset="utf-8">
<title>Selkirk Boat Lines and Freight – Business Card</title>
<link rel="stylesheet" href="https://fonts.googleapis.com/css2?family=Roboto:wght@300;400;700&display=swap">
<style>
  :root {
    --backdrop: #3b3b3b;
    --card: #ffffff;
    --ocean: #0e57a6;
    --accent: #f78f20;
    --steel-light: #e2e4e6;
    --steel-dark: #8c9094;
    --rule: #9a9a9a;
    --brand-blue: #0e57a6;
  }
  * { margin: 0; padding: 0; box-sizing: border-box; }
  html, body {
    width: 1105px; height: 1200px; overflow: hidden;
    background: var(--backdrop);
    font-family: "Roboto", Arial, sans-serif;
  }
  .card {
    position: absolute; left: 192px;
    width: 720px; height: 410px;
    background: var(--card); overflow: hidden;
  }
  .card--front { top: 167px; }
  .card--back { top: 623px; }
  .card-art { position: absolute; inset: 0; }

  .holder {
    position: absolute; right: 396px; top: 302px; text-align: right;
  }
  .holder-name {
    color: var(--accent); font-weight: 700; font-size: 25px; letter-spacing: 0.5px;
  }
  .holder-title {
    color: #fff; font-weight: 300; font-size: 21px; margin-top: 6px;
  }
  .divider {
    position: absolute; left: 345px; top: 296px; width: 1px; height: 80px; background: #fff;
  }
  .contacts { position: absolute; left: 372px; top: 290px; list-style: none; }
  .contacts li {
    display: flex; align-items: center; height: 27.5px;
    color: #fff; font-size: 18px; font-weight: 300;
  }
  .contacts svg { width: 17px; height: 17px; margin-right: 12px; flex: none; }

  .brand {
    position: absolute; left: 0; right: 0; top: 208px; text-align: center;
    color: var(--brand-blue); font-weight: 700;
  }
  .brand-name { font-size: 56px; line-height: 1; letter-spacing: 1px; }
  .brand-tagline { font-size: 20px; line-height: 1; margin-top: 10px; }

  .back-rule {
    position: absolute; left: 225px; top: 352px; width: 270px; height: 1px; background: var(--rule);
  }
</style>
</head>
<body>
  <section class="card card--front">
    <svg class="card-art" viewBox="0 0 720 410" width="720" height="410">
      <defs>
        <linearGradient id="steel" x1="0" y1="0" x2="0" y2="1">
          <stop offset="0" stop-color="var(--steel-light)"/>
          <stop offset="1" stop-color="var(--steel-dark)"/>
        </linearGradient>
      </defs>
      <rect role="img" aria-label="Illustration of a grey water taxi boat on the water"
            x="122" y="25" width="463" height="225" rx="10" fill="url(#steel)"/>
      <path d="M0 232 C200 200 450 212 720 220 L720 410 L0 410 Z" fill="var(--ocean)"/>
    </svg>

    <div class="holder">
      <div class="holder-name">MARCUS HOLLEND</div>
      <div class="holder-title">Captain</div>
    </div>
    <div class="divider"></div>
    <ul class="contacts">
      <li>
        <svg viewBox="0 0 24 24"><path fill="var(--accent)" d="M6.6 10.8a15.1 15.1 0 0 0 6.6 6.6l2.2-2.2c.3-.3.7-.4 1-.2 1.1.4 2.3.6 3.6.6.6 0 1 .4 1 1V20c0 .6-.4 1-1 1A17 17 0 0 1 3 4c0-.6.4-1 1-1h3.5c.6 0 1 .4 1 1 0 1.3.2 2.5.6 3.6.1.3 0 .7-.2 1z"/></svg>
        555 214 7390
      </li>
      <li>
        <svg viewBox="0 0 24 24"><rect x="2" y="5" width="20" height="14" rx="2" fill="var(--accent)"/><path d="M3 6l9 7 9-7" stroke="var(--ocean)" stroke-width="1.6" fill="none"/></svg>
        marcus@selkirkboatlines.com
      </li>
      <li>
        <svg viewBox="0 0 24 24"><circle cx="12" cy="12" r="10" fill="var(--accent)"/><path d="M2 12h20M12 2c3 3 3 17 0 20M12 2c-3 3-3 17 0 20" stroke="var(--ocean)" stroke-width="1.4" fill="none"/></svg>
        www.selkirkboatlines.com
      </li>
    </ul>
  </section>

  <section class="card card--back">
    <div class="brand">
      <div class="brand-name">SELKIRK</div>
      <div class="brand-tagline">Boat Lines and Freight</div>
    </div>
    <div class="back-rule"></div>
  </section>
</body>
</html>
```